Letterhead design for Sleep Consulting Business

I'm looking for a new letterhead (heading/footer) design for my Sleep Consulting Business, I work with families to help their children improve their sleep.

The heading/footer will used in Microsoft Word Only-to be used for all of my documents such as writing Sleep Plans. I need to utilize as much working space in the document as possible. This will NOT be printed out on paper- it will only be used for heading/footer on microsoft word, then emailed to clients, who may print it at home.

My brand colors:
Dark Blue Hex: 1F2A42
Lighter Blueish Hex: 90BEC9
You're welcome to check out my website for inspiration- it is freshly created with other colors as well, and I love the outcome. www.hollowpinerest.com

Target Market(s)

Tired parents

Font styles to use
Script
Other font styles liked:
• Great Vibe, Lato or Just Another Hand are all used currently for my brand. Open to other options.

Requirements
Must have
• The letterhead (heading/footer) MUST be kept narrow (height-wise), so I have plenty of space on my document, while including important information.

It should look professional on screen, and when printed.

Must include my business name OR logo (Hollow Pine Sleep Consulting), and my email address. Mara@hollowpinerest.com

Website is optional, not required, just if you need to fill in a spot: www.hollowpinerest.com

```html
<!DOCTYPE html>
<html lang="en">
<head>
<meta charset="utf-8">
<title>Hollow Pine Sleep Consulting – Letterhead</title>
<link href="https://fonts.googleapis.com/css2?family=Poppins:wght@300;400&display=swap" rel="stylesheet">
<style>
  :root {
    --navy: #1F2A42;
    --mist: #90BEC9;
    --paper: #F2F2F2;
    --backdrop: #DDE1E3;
    --watermark: #E4E8EA;
  }
  * { margin: 0; padding: 0; box-sizing: border-box; }
  html, body {
    width: 1200px;
    height: 1200px;
    overflow: hidden;
    background: var(--backdrop);
    font-family: "Poppins", sans-serif;
  }
  .letterhead {
    position: absolute;
    left: 200px;
    top: 35px;
    width: 800px;
    height: 1130px;
    background: var(--paper);
    box-shadow: 0 4px 14px rgba(31, 42, 66, 0.12);
    overflow: hidden;
  }
  .header {
    position: absolute;
    left: 42px;
    top: 44px;
    display: flex;
    align-items: center;
    gap: 16px;
  }
  .header__mark {
    width: 50px;
    height: 50px;
    border-radius: 50%;
    background: var(--mist);
  }
  .header__name {
    color: var(--navy);
    font-weight: 400;
    line-height: 1.15;
  }
  .header__title { font-size: 25px; }
  .header__subtitle { font-size: 10px; letter-spacing: 3px; }
  .watermark {
    position: absolute;
    left: 191px;
    top: 357px;
    width: 418px;
    height: 418px;
    border-radius: 50%;
    background: var(--watermark);
  }
  .footer {
    position: absolute;
    left: 0;
    bottom: 0;
    width: 800px;
    height: 113px;
  }
  .footer__waves {
    position: absolute;
    inset: 0;
    width: 100%;
    height: 100%;
  }
  .footer__contacts {
    position: absolute;
    left: 32px;
    bottom: 18px;
    list-style: none;
    color: #ffffff;
    font-weight: 300;
    font-size: 13.5px;
    line-height: 19px;
  }
  .footer__contacts li {
    display: flex;
    align-items: center;
    gap: 10px;
  }
  .footer__icon { width: 12px; height: 12px; flex: none; }
</style>
</head>
<body>
  <main class="letterhead">
    <header class="header">
      <div class="header__mark"></div>
      <div class="header__name">
        <div class="header__title">Hollow Pine</div>
        <div class="header__subtitle">SLEEP CONSULTING</div>
      </div>
    </header>

    <div class="watermark" role="img" aria-label="Faint brand emblem watermark"></div>

    <footer class="footer">
      <svg class="footer__waves" viewBox="0 0 955 135" preserveAspectRatio="none" aria-hidden="true">
        <path fill="#90BEC9" d="M0,2 C130,-2 270,30 362,58 C250,36 120,32 0,36 Z"/>
        <path fill="#1F2A42" d="M0,44 C120,36 260,42 380,64 C480,84 560,104 650,106 C800,108 900,90 955,70 L955,135 L0,135 Z"/>
        <path fill="#90BEC9" d="M600,100 C780,100 900,70 955,32 L955,62 C880,92 760,104 600,102 Z"/>
      </svg>
      <ul class="footer__contacts">
        <li>
          <svg class="footer__icon" viewBox="0 0 12 12" aria-hidden="true">
            <rect x="0.5" y="2" width="11" height="8" fill="#90BEC9"/>
            <path d="M0.5,2.5 L6,6.5 L11.5,2.5" fill="none" stroke="#1F2A42" stroke-width="1"/>
          </svg>
          Mara@hollowpinerest.com
        </li>
        <li>
          <svg class="footer__icon" viewBox="0 0 12 12" aria-hidden="true">
            <circle cx="6" cy="6" r="5.2" fill="#90BEC9"/>
            <path d="M1,6 H11 M6,1 C3.5,3.5 3.5,8.5 6,11 M6,1 C8.5,3.5 8.5,8.5 6,11" fill="none" stroke="#1F2A42" stroke-width="0.9"/>
          </svg>
          www.hollowpinerest.com
        </li>
      </ul>
    </footer>
  </main>
</body>
</html>
```